Tri-Fold Behavioral Health (Addiction) Agency Brochure

We need an updated and refreshed brochure design for our Residential Treatment Facilities. These facilities provide residential comprehensive treatment for those struggling with drug and alcohol addiction along with those who are dually diagnosed with mental health issues as well. We are starting with this brochure but plan to have our other brochures "match" the design and will submit that following completion of this design. I have attached a "Brochure Areas" document that is numbered and corresponds to the brochure areas of our current brochure. We have modified the wording in each of these areas so the wording in the attached word document is what needs to go on the design (not the words in the attached pictures of our current brochure). We want something that is a professional design look. The front page of the brochure needs to have our main agency Logo/Name: Maple Hollow Behavioral Health Partners (logo attached). The back page we would like to have the two locations listed with the address (possible map if able). The first is called: The Harbor at Maple Hollow - located at 7214 Tolliver Lane, Frazeysburg OH 43829. The Second Facility is called: The Brennick at Maple Hollow - located at 618 Garvin St, Zanesville OH 43708. I have also attached some pictures of our facilities that can be used. They all don't have to be used and we would still like some stock photos of "people" or group counseling, etc.

Requirements
Must have
• Need final design file to be publisher or word along with pdf and or other print type file.
Nice to have
• I have also attached the current booth design photo that we are using to possibly match design look.

```html
<!DOCTYPE html>
<html lang="en">
<head>
<meta charset="UTF-8">
<title>Maple Hollow Residential Treatment – Inside Spread</title>
<link rel="stylesheet" href="https://fonts.googleapis.com/css2?family=Montserrat:wght@500;600;700;800&family=Arimo:wght@400&display=swap">
<style>
  :root {
    --bg: #6f6f6f;
    --ink-dark: #222325;
    --teal: #22b3b0;
    --teal-deep: #1a9c9a;
    --mint: #d5ecea;
    --white: #ffffff;
    --text-dark: #1f2326;
    --photo-warm-a: #8a5a34;
    --photo-warm-b: #3a2416;
    --photo-green-a: #7ea65a;
    --photo-green-b: #3f5e33;
  }
  * { margin: 0; padding: 0; box-sizing: border-box; }
  html, body { width: 1200px; height: 800px; overflow: hidden; background: var(--bg); }
  .spread {
    position: absolute; left: 30px; top: 30px;
    width: 1140px; height: 740px;
    background: var(--mint);
    overflow: hidden;
    box-shadow: 0 10px 30px rgba(0,0,0,.25);
  }
  .spread-shapes { position: absolute; inset: 0; }
  .fold { stroke: rgba(0,0,0,.08); stroke-width: 1; }

  .block { position: absolute; }
  .section-head { display: flex; align-items: flex-end; gap: 10px; }
  .section-num {
    font-family: "Montserrat", sans-serif; font-weight: 800;
    font-size: 46px; line-height: .8;
  }
  .section-title {
    font-family: "Montserrat", sans-serif; font-weight: 700;
    font-size: 18px; line-height: 1.1; padding-bottom: 2px;
  }
  .rule { position: absolute; height: 2px; background: var(--teal); }
  .body-copy {
    font-family: "Arimo", Arial, sans-serif;
    font-size: 11.5px; line-height: 1.3; text-align: justify;
    margin-top: 12px;
  }

  .experience { left: 24px; top: 38px; width: 330px; color: var(--white); }
  .experience .rule { left: 28px; top: -8px; width: 210px; }
  .dual { left: 24px; top: 352px; width: 330px; color: var(--white); }
  .dual .section-title { text-transform: uppercase; font-size: 17px; }
  .programming { left: 404px; top: 332px; width: 334px; color: var(--text-dark); }
  .programming .section-title { color: var(--teal); }
  .programming .rule { left: 44px; top: -10px; width: 230px; }

  .bullet-list { list-style: none; font-family: "Montserrat", sans-serif; font-weight: 500; }
  .bullet-list li { position: relative; padding-left: 20px; font-size: 14px; line-height: 1.35; }
  .bullet-list li::before {
    content: ""; position: absolute; left: 0; top: 5px;
    width: 11px; height: 11px; border-radius: 50%;
  }
  .bullet-list li::after {
    content: ""; position: absolute; left: 3px; top: 8.5px;
    width: 3px; height: 3px;
    border-right: 1.5px solid var(--white); border-top: 1.5px solid var(--white);
    transform: rotate(45deg);
  }
  .services { left: 786px; top: 262px; color: var(--text-dark); }
  .services li::before { background: var(--teal); }
  .groups { left: 948px; top: 420px; width: 186px; color: var(--white); }
  .groups-title {
    font-family: "Montserrat", sans-serif; font-weight: 700; font-size: 17px;
    margin-bottom: 6px;
  }
  .groups .bullet-list li { font-size: 13px; }
  .groups .bullet-list li::before { background: var(--ink-dark); top: 4px; }
  .groups .bullet-list li::after { top: 7.5px; }
</style>
</head>
<body>
<main class="spread">
  <svg class="spread-shapes" width="1140" height="740" viewBox="0 0 1140 740">
    <defs>
      <linearGradient id="warmRoom" x1="0" y1="0" x2="1" y2="1">
        <stop offset="0" stop-color="var(--photo-warm-a)"/>
        <stop offset="1" stop-color="var(--photo-warm-b)"/>
      </linearGradient>
      <linearGradient id="bedroom" x1="0" y1="0" x2="1" y2="1">
        <stop offset="0" stop-color="#d9b57c"/>
        <stop offset="1" stop-color="#5a3620"/>
      </linearGradient>
      <linearGradient id="garden" x1="0" y1="0" x2="0" y2="1">
        <stop offset="0" stop-color="var(--photo-green-a)"/>
        <stop offset="1" stop-color="var(--photo-green-b)"/>
      </linearGradient>
    </defs>

    <!-- Panel 1 -->
    <path d="M0 0 H380 V262 Q200 292 0 300 Z" fill="var(--ink-dark)"/>
    <path d="M0 328 Q200 322 380 288 V740 H0 Z" fill="var(--teal)"/>
    <g role="img" aria-label="Photo of a facility living room with sofas, armchairs and fireplace">
      <rect x="30" y="532" width="320" height="170" fill="url(#warmRoom)"/>
    </g>
    <path d="M30 556 h10 l-2 12 l2 12 h-10 Z" fill="var(--teal)"/>
    <path d="M33 563 l4 5 l-4 5" stroke="var(--white)" stroke-width="1.6" fill="none"/>

    <!-- Panel 2 -->
    <path d="M380 0 H760 V215 Q570 250 380 282 Z" fill="var(--ink-dark)"/>
    <g role="img" aria-label="Photo of a wood-paneled lounge with fireplace and couches">
      <path d="M405 25 H740 V258 Q580 276 405 302 Z" fill="url(#warmRoom)"/>
    </g>
    <path d="M405 302 Q580 276 740 258" stroke="var(--teal)" stroke-width="6" fill="none"/>
    <circle cx="428" cy="50" r="10" fill="var(--teal)"/>
    <path d="M426 45 l4 5 l-4 5" stroke="var(--white)" stroke-width="1.8" fill="none"/>
    <g role="img" aria-label="Photo of the facility garden, lawn and cottage exterior">
      <path d="M380 522 Q660 508 940 496 V740 H380 Z" fill="url(#garden)"/>
    </g>

    <!-- Panel 3 -->
    <path d="M760 0 H1140 V150 Q950 215 760 245 Z" fill="var(--ink-dark)"/>
    <g role="img" aria-label="Photo of a resident bedroom with two beds">
      <path d="M782 25 H1118 V150 Q950 200 782 228 Z" fill="url(#bedroom)"/>
    </g>
    <path d="M782 232 Q950 205 1118 154" stroke="var(--teal)" stroke-width="6" fill="none"/>
    <path d="M870 228 Q1000 210 1118 180" stroke="var(--teal)" stroke-width="1.2" fill="none"/>
    <circle cx="804" cy="50" r="10" fill="var(--teal)"/>
    <path d="M802 45 l4 5 l-4 5" stroke="var(--white)" stroke-width="1.8" fill="none"/>
    <path d="M930 420 Q1040 405 1140 380 V740 H930 Z" fill="var(--teal)"/>
    <path d="M940 496 V740" stroke="var(--teal)" stroke-width="0"/>

    <line class="fold" x1="380" y1="0" x2="380" y2="740"/>
    <line class="fold" x1="760" y1="0" x2="760" y2="740"/>
  </svg>

  <section class="block experience">
    <span class="rule"></span>
    <div class="section-head">
      <span class="section-num">1</span>
      <h2 class="section-title">The Experience</h2>
    </div>
    <p class="body-copy">Residential Treatment at Maple Hollow offers intensive structured treatment services for men and women suffering from substance abuse disorders in a 24-hour medically monitored Long-term residential treatment facility. Our treatment facilities offer clients the ability to feel welcomed, accepted and supported in a retreat like setting. Our multi-disciplinary team consists of Physicians, Therapists, Nurses, Case Managers, and other Recovery Support Specialists, allowing for each individual's physical, social, mental, and emotional development.</p>
  </section>

  <section class="block dual">
    <div class="section-head">
      <span class="section-num">2</span>
      <h2 class="section-title">Dual Diagnosis</h2>
    </div>
    <p class="body-copy">It is an unfortunate reality that many individuals who struggle with addiction are also faced with mental illness. Our residential treatment programs support dually-diagnosed individuals by providing onsite psychiatric evaluations, regular psychiatric follow-ups, medication management, and therapy services aimed at treating these symptoms as a part of the client's individualized treatment plan.</p>
  </section>

  <section class="block programming">
    <span class="rule"></span>
    <div class="section-head">
      <span class="section-num">3</span>
      <h2 class="section-title">Our Programming</h2>
    </div>
    <p class="body-copy">Residential treatment programing provides comprehensive treatment for those struggling with drug and alcohol addiction along with those who are dually diagnosed with mental health issues as well. Residents will be able to experience an evidence-based program model inclusive of:</p>
  </section>

  <ul class="block bullet-list services">
    <li>Comprehensive Evaluations</li>
    <li>Treatment Team Collaboration</li>
    <li>Medication Management</li>
    <li>Aftercare Planning</li>
    <li>Individual Therapy</li>
    <li>Family Therapy</li>
    <li>Group Therapy</li>
  </ul>

  <section class="block groups">
    <h3 class="groups-title">Groups</h3>
    <ul class="bullet-list">
      <li>Psychoeducational</li>
      <li>Psychotherapy</li>
      <li>Health &amp; Wellness</li>
      <li>Independent Living Skills</li>
      <li>Peer-Led (AA/NA)</li>
      <li>Grief &amp; Loss</li>
      <li>Codependency</li>
      <li>Stress Management</li>
    </ul>
  </section>
</main>
</body>
</html>
```